Coastal Silken Hair Weaves needs a packaging design

We need a packaging design for a new hair extension company based in Edmonton, Alberta called Velvet Crest. Our packaging should communicate high quality, luxurious hair that will never tangle or dry out. The product will be marketed to salon professionals as well as clients. We would like to see designs that include but not restricted to the colours gold black and white.
Updates

Reason: Although we were very impressed with the designs that came though thus far, we are hoping to receive a few more ideas before making a final decision. Thank you!

Target Market(s)

Women and beauty industry professionals. High end market.

Industry/Entity Type

Hair

Requirements
Must have
• "Highest quality 100% Remi hair!" should be written on the front of the package. In addition, we would like to add text to the back of the packaging as follows:
• Hair Collection and Color Processing:
• Only the highest quality hair is selected which ensures high moisture and nutrient content
• The hair is directly cut from the donor which ensures that the hair cuticle remains intact and always tangle-free
• No chemicals are used in dyeing the hair
• The hair will never fade due to the mild and healthy herbal extract used in the dyeing process which gently penetrates to the inner core of the hair
• Care Instructions:
• Velvet Crest provides only the highest in quality Remi hair that demands very little care to maintain it’s luxurious feel.
• Use a proper extension bristle brush
• Wash the hair with a sulfate-free shampoo and follow with a moisturizing conditioner that is formulated for hair extensions
• Do not apply any type of chemicals to the hair
• We proudly show our immense passion for delivering superior quality in our full product line.
• We insist that it is important for you to know and understand what you are purchasing in your hair extensions. We guarantee the highest quality of our products.
• Velvet Crest is strongly committed to serving their clients with utmost integrity, believing in a foundation of personal and professional ethics and our 20 years service in the beauty industry.
Nice to have
• I would like the background to be white with the "C" in gold. My concern is that this may look too plain, but with that said, I don't want the design to be too busy. Keeping it classy is my main goal.

```html
<!DOCTYPE html>
<html lang="en">
<head>
<meta charset="utf-8">
<title>Velvet Crest – Packaging</title>
<link href="https://fonts.googleapis.com/css2?family=Great+Vibes&family=Arimo:wght@400;600&display=swap" rel="stylesheet">
<style>
  :root {
    --frame: #e4e4e4;
    --black: #000000;
    --white: #ffffff;
    --panel-grey: #b3b3b3;
    --sleeve-light: #e5e5e5;
    --orange-deep: #ff9800;
    --orange-core: #ffc20a;
    --gold: #d49a2a;
    --gold-light: #fff200;
    --pink: #d9336b;
    --script-pink: #ec1c5a;
    --string: #9a9a9a;
  }
  html, body { margin: 0; padding: 0; overflow: hidden; background: var(--white); }
  .canvas {
    position: relative; width: 1001px; height: 1200px; overflow: hidden;
    background: var(--white); box-sizing: border-box;
    border: 3px solid var(--frame);
  }
  .artwork { position: absolute; inset: 0; }
  .brand-name {
    position: absolute; margin: 0; text-align: center;
    font-family: "Great Vibes", cursive; font-weight: 400; color: var(--black);
    line-height: 1; white-space: nowrap;
  }
  .header-name { color: var(--white); font-size: 34px; left: 193px; width: 324px; top: 48px; }
  .tagline {
    position: absolute; margin: 0; text-align: center; white-space: nowrap;
    font-family: "Great Vibes", cursive; color: var(--script-pink); line-height: 1;
  }
  .claims {
    position: absolute; margin: 0; text-align: center; white-space: nowrap;
    font-family: "Arimo", Arial, sans-serif; font-size: 12.5px; color: var(--black);
    letter-spacing: 0.1px;
  }
  .claims .dot { display: inline-block; width: 5px; height: 5px; background: var(--black); margin: 0 4px 2px; }
  .badge-new {
    position: absolute; left: 196px; top: 170px; transform: rotate(-35deg);
    font-family: "Arimo", Arial, sans-serif; font-weight: 600; font-size: 17px;
    color: var(--white); letter-spacing: 1px;
  }
  .pack-name { font-size: 50px; left: 188px; width: 327px; top: 312px; }
  .pack-tagline { font-size: 27px; left: 188px; width: 327px; top: 366px; }
  .pack-claims { left: 188px; width: 327px; top: 398px; }
  .tag-name { font-size: 50px; left: 494px; width: 316px; top: 978px; }
  .tag-tagline { font-size: 27px; left: 494px; width: 316px; top: 1030px; }
  .tag-claims { left: 494px; width: 316px; top: 1058px; }
</style>
</head>
<body>
<main class="canvas">
  <svg class="artwork" width="1001" height="1200" viewBox="0 0 1001 1200" aria-hidden="true">
    <defs>
      <linearGradient id="accentStrip" x1="0" x2="1">
        <stop offset="0" stop-color="var(--pink)"/>
        <stop offset="0.35" stop-color="#e8a03a"/>
        <stop offset="0.6" stop-color="var(--gold-light)"/>
        <stop offset="0.85" stop-color="#e3892a"/>
        <stop offset="1" stop-color="var(--gold)"/>
      </linearGradient>
      <linearGradient id="sleeveFade" x1="0" y1="0" x2="0" y2="1">
        <stop offset="0" stop-color="var(--white)"/>
        <stop offset="0.3" stop-color="var(--sleeve-light)"/>
        <stop offset="1" stop-color="var(--sleeve-light)"/>
      </linearGradient>
      <radialGradient id="orangeGlow" cx="0.5" cy="0.5" r="0.6">
        <stop offset="0" stop-color="var(--orange-core)"/>
        <stop offset="1" stop-color="var(--orange-deep)"/>
      </radialGradient>
      <linearGradient id="goldRim" x1="0" y1="0" x2="1" y2="1">
        <stop offset="0" stop-color="var(--gold)"/>
        <stop offset="0.45" stop-color="var(--gold-light)"/>
        <stop offset="0.7" stop-color="var(--gold)"/>
        <stop offset="1" stop-color="#c9892c"/>
      </linearGradient>
    </defs>

    <!-- package header -->
    <rect class="pack-header" x="193" y="38" width="324" height="60" fill="var(--black)"/>
    <rect class="pack-accent" x="193" y="98" width="324" height="7" fill="url(#accentStrip)"/>

    <!-- package sleeve -->
    <rect class="pack-sleeve" x="186" y="113" width="331" height="1050" fill="url(#sleeveFade)"/>
    <path class="pack-window-shadow" d="M190,118 H514 V560 Q514,636 352,636 Q190,636 190,560 Z" fill="#dedede"/>
    <path class="pack-window" d="M190,118 H514 V540 Q514,624 352,624 Q190,624 190,540 Z" fill="var(--panel-grey)" stroke="#d8d8d8" stroke-width="3"/>

    <!-- front label -->
    <path class="label-rim-gold" d="M188,152 Q300,132 420,140 Q515,150 518,250 L518,528 Q360,532 250,515 Q188,505 188,420 Z" fill="url(#goldRim)"/>
    <path class="label-rim-dark" d="M188,152 Q300,136 410,144 Q505,152 512,250 L514,522 Q360,526 250,508 Q188,496 188,420 Z" fill="#2b2b2b"/>
    <path class="label-face" d="M188,152 Q300,138 400,146 Q495,156 500,250 L515,518 Q360,520 250,500 Q190,486 188,410 Z" fill="url(#orangeGlow)"/>
    <path class="label-new-corner" d="M188,152 L268,150 L188,212 Z" fill="var(--pink)"/>

    <!-- brand mark placeholder on label -->
    <circle class="mark-dot" cx="352" cy="262" r="26" fill="var(--gold)"/>

    <!-- hang tag string -->
    <path class="tag-string" d="M652,862 Q635,760 628,640 L614,450 Q610,405 680,405 Q748,405 745,450 L718,800 Q716,830 706,848" fill="none" stroke="var(--string)" stroke-width="5" stroke-linecap="round"/>

    <!-- hang tag -->
    <circle class="tag-rim" cx="652" cy="998" r="158" fill="url(#goldRim)"/>
    <circle class="tag-face" cx="652" cy="998" r="146" fill="url(#orangeGlow)"/>
    <circle class="tag-hole" cx="652" cy="864" r="5" fill="var(--white)" stroke="var(--string)" stroke-width="1.5"/>
    <circle class="mark-dot" cx="652" cy="930" r="26" fill="var(--gold)"/>
  </svg>

  <p class="brand-name header-name">Velvet Crest</p>

  <span class="badge-new">NEW</span>
  <p class="brand-name pack-name">Velvet Crest</p>
  <p class="tagline pack-tagline">Premium Hair Extension</p>
  <p class="claims pack-claims">HIGH QUALITY<span class="dot"></span>LUXURIOUS<span class="dot"></span>NO TANGLES</p>

  <p class="brand-name tag-name">Velvet Crest</p>
  <p class="tagline tag-tagline">Premium Hair Extension</p>
  <p class="claims tag-claims">HIGH QUALITY<span class="dot"></span>LUXURIOUS<span class="dot"></span>NO TANGLES</p>
</main>
</body>
</html>
```